Ecommerce site for Bramwell Dovey Company

This is an ecommerce store design and will be based on the xcart ecommerce platform, attached is a design specification and all images to use in the design, you may use any other images you see fit.
This is a new Company so has no logo, if possible please create a logo but if not just use a text based logo in the design this maybe replaced later if required.
We only require a Home page design initially but will also need a category and product page design created, if you can do those also it would be an advantage.
IMPORTANT
We require all designs to be supplied as a full size JPG so we can see the design in detail as the pixel quarry previews are often too small.

```html
<!DOCTYPE html>
<html lang="en">
<head>
<meta charset="utf-8">
<title>Dovey Tracks — Home</title>
<link rel="stylesheet" href="https://fonts.googleapis.com/css2?family=Fira+Sans+Condensed:ital,wght@0,400;0,500;1,300&family=Open+Sans:wght@400;600&display=swap">
<style>
  :root {
    --page-top: #f8f8f9;
    --page-bottom: #e2e2e3;
    --ink: #6b6b6b;
    --ink-dark: #4a4a4a;
    --logo-grey: #707070;
    --search-bg: #d3d4d6;
    --panel-bar: #868789;
    --sidebar-bg: #ffffff;
    --active-bg: #e6e7e9;
    --pay-bg: #e4e5e9;
    --promo-bg: #999794;
    --about-dark: #696969;
    --about-light: #b3b3b3;
    --light-text: #f4f4f4;
    --photo-a1: #e9e9eb;
    --photo-a2: #9b9a7a;
    --photo-b1: #dfe6e8;
    --photo-b2: #1f5f66;
  }
  * { margin: 0; padding: 0; box-sizing: border-box; }
  html, body { width: 1200px; height: 780px; overflow: hidden; }
  body {
    background: linear-gradient(var(--page-top), var(--page-bottom));
    font-family: "Open Sans", sans-serif;
    color: var(--ink);
    position: relative;
  }
  .brand {
    position: absolute; left: 144px; top: 40px;
    font-family: "Fira Sans Condensed", sans-serif;
    font-weight: 500; font-size: 42px; letter-spacing: -1px;
    color: var(--logo-grey);
  }
  .search {
    position: absolute; left: 900px; top: 20px; width: 152px; height: 24px;
    background: var(--search-bg); display: flex; align-items: center;
  }
  .search span { flex: 1; font-size: 12px; color: #666; padding-left: 8px; }
  .search .search-btn {
    width: 26px; height: 24px; border-left: 1px solid #eee;
    display: flex; align-items: center; justify-content: center;
  }
  .cart {
    position: absolute; right: 148px; top: 57px; text-align: right;
    font-size: 10.5px; line-height: 13px; color: var(--ink-dark);
  }
  .cart b { font-weight: 600; }
  .cart .cart-links { font-size: 9px; font-weight: 600; }
  .cart .cart-links a { color: var(--ink-dark); text-decoration: underline; margin-left: 10px; }
  .main-nav {
    position: absolute; left: 0; width: 1200px; top: 115px;
    text-align: center; font-size: 12px; color: var(--ink);
  }
  .main-nav a { color: var(--ink); text-decoration: none; }
  .main-nav .sep { margin: 0 12px; }
  .panel {
    position: absolute; left: 146px; top: 144px; width: 906px; height: 600px;
    border-radius: 0 0 28px 28px; overflow: hidden;
    box-shadow: 0 4px 8px rgba(0,0,0,0.25);
    display: grid; grid-template-columns: 174px 366px 366px; grid-template-rows: 307px 293px;
  }
  .sidebar { background: var(--sidebar-bg); border-top: 7px solid var(--panel-bar); position: relative; }
  .category-list { list-style: none; margin-top: 44px; }
  .category-list li {
    height: 33px; line-height: 33px; padding-left: 18px; margin-bottom: 16px;
    font-size: 14px; color: #7b7b7b;
  }
  .category-list li.active { background: var(--active-bg); color: var(--ink-dark); }
  .photo-tracks { background: linear-gradient(135deg, var(--photo-a1) 20%, #c7c3a8 55%, var(--photo-a2)); }
  .photo-room { background: linear-gradient(90deg, var(--photo-b1) 30%, #86aeb3 60%, var(--photo-b2)); }
  .payments { background: var(--pay-bg); position: relative; }
  .pay-grid { position: absolute; left: 34px; top: 90px; width: 106px; display: grid; grid-template-columns: 50px 50px; gap: 6px; }
  .pay-card { height: 32px; border: 1px solid #b5b5b8; background: #f2f2f4; }
  .pay-wide { position: absolute; left: 46px; top: 166px; width: 84px; height: 31px; border: 1px solid #a9a9ad; background: #f2f2f4; }
  .promo { background: var(--promo-bg); padding: 48px 0 0 27px; }
  .promo ul { list-style: none; }
  .promo li {
    font-family: "Fira Sans Condensed", sans-serif; font-style: italic; font-weight: 300;
    font-size: 19px; line-height: 19px; color: var(--light-text);
    padding-left: 11px; position: relative; margin-bottom: 18px;
  }
  .promo li::before { content: "•"; position: absolute; left: 0; font-size: 14px; }
  .about {
    background: linear-gradient(150deg, var(--about-dark) 60%, var(--about-light) 100%);
    padding: 66px 32px 0 32px; position: relative;
  }
  .about p {
    font-family: "Fira Sans Condensed", sans-serif; font-size: 12.5px; line-height: 18px;
    color: var(--light-text); text-align: justify; margin-bottom: 6px;
  }
  .about .brand-small {
    position: absolute; right: 22px; bottom: 18px;
    font-family: "Fira Sans Condensed", sans-serif; font-weight: 500; font-size: 22px;
    letter-spacing: -0.5px; color: #6e6e6e;
  }
</style>
</head>
<body>
  <div class="brand">Dovey Tracks</div>

  <div class="search">
    <span>search...</span>
    <div class="search-btn">
      <svg width="14" height="14" viewBox="0 0 14 14" aria-hidden="true">
        <circle cx="5.5" cy="5.5" r="4" fill="none" stroke="#5a5a5a" stroke-width="2"/>
        <line x1="8.5" y1="8.5" x2="12.5" y2="12.5" stroke="#5a5a5a" stroke-width="2.4"/>
      </svg>
    </div>
  </div>

  <div class="cart">
    <div><b>CART:</b> 2 products</div>
    <div>Total price: $100</div>
    <div class="cart-links"><a href="#">view cart »</a><a href="#">check cart »</a></div>
  </div>

  <nav class="main-nav">
    <a href="#">HOME</a><span class="sep">|</span><a href="#">ABOUT US</a><span class="sep">|</span><a href="#">DELIVERY TERMS</a><span class="sep">|</span><a href="#">TESTIMONIALS</a><span class="sep">|</span><a href="#">FAQ'S</a><span class="sep">|</span><a href="#">CONTACT US</a>
  </nav>

  <main class="panel">
    <aside class="sidebar">
      <ul class="category-list">
        <li class="active">Quiet Glide Tracks</li>
        <li>Hand operated Tracks</li>
        <li>Cord operated Tracks</li>
        <li>Automated Tracks</li>
      </ul>
    </aside>
    <div class="photo-tracks" role="img" aria-label="Curtain poles with glass square finials in various finishes beside orchid flowers"></div>
    <div class="photo-room" role="img" aria-label="Bright room with tall windows and teal curtains on a bay track"></div>

    <div class="payments">
      <div class="pay-grid">
        <div class="pay-card"></div><div class="pay-card"></div>
        <div class="pay-card"></div><div class="pay-card"></div>
      </div>
      <div class="pay-wide"></div>
    </div>

    <section class="promo">
      <ul>
        <li>Free UK delivery on orders<br>over £100</li>
        <li>Over 20 years experience<br>measuring / making / fitting</li>
        <li>5 years guarantee on all quiet glide<br>products</li>
        <li>Friendly family run business</li>
      </ul>
    </section>

    <section class="about">
      <p>From our Worcestershire factory we have been supplying quality product to British customers for over 30 years. We pride ourselves on the fact that whilst we refuse to compromise on quality, we still manage to offer our product at unbeatable prices.</p>
      <p>We take immense pride in our made to measure wooden venetian blinds, as well as our entire window decor range. When you think of made to measure wooden venetian blinds, think of us.</p>
      <div class="brand-small">Dovey Tracks</div>
    </section>
  </main>
</body>
</html>
```